IT Consulting Business Card Design

We need a business card on our company name....which is a IT consulting and staffing company. We also train masters graduates in various IT courses. 70% of the time these cards will be handed out to the graduate students at the universities. 30% for our clients and business partners. We are uploading our company logo...would like to see something that matches our logo or blends with it. Please visit www.brightlanetek.example for more details on logo and colors.

Target Market(s)

70% of the time these cards will be handed out to the graduate students at the universities. 30% for our clients and business partners.

Industry/Entity Type

Business

Contact Information for Business Card

Rafe Tolliverson
Vice-President
Bright Lane Tek Inc
3187 Winslow Drive, Suite 412
Oak Hollow, NJ 07391
rafe@brightlanetek.example
Office : 1-855-217-9038 X 414
Cell number : 908-731-2948

Requirements
Nice to have
• may be company logo and name on the back of the card and detials on the other side...just a thought..!!

```html
<!DOCTYPE html>
<html lang="en">
<head>
<meta charset="utf-8">
<title>Bright Lane Tek – Business Card</title>
<link href="https://fonts.googleapis.com/css2?family=Fira+Sans+Extra+Condensed:wght@700&family=EB+Garamond:wght@400&display=swap" rel="stylesheet">
<style>
  :root {
    --ink-black: #080a0a;
    --panel-light: #e2e9e6;
    --brand-red: #ee0d0d;
    --box-red: #f01a18;
    --brand-dark: #2a2e30;
    --paper-white: #ffffff;
  }
  html, body {
    margin: 0;
    padding: 0;
    overflow: hidden;
    background: var(--ink-black);
  }
  .canvas {
    position: relative;
    width: 1019px;
    height: 1200px;
    background: var(--ink-black);
    overflow: hidden;
  }
  .card-front {
    position: absolute;
    left: 0;
    top: 41px;
    width: 1019px;
    height: 516px;
    background: var(--panel-light);
  }
  .front-mark {
    position: absolute;
    left: 43px;
    top: 135px;
    width: 244px;
    height: 244px;
  }
  .front-wordmark {
    position: absolute;
    left: 326px;
    top: 256px;
    margin: 0;
    font-family: "Fira Sans Extra Condensed", "Arial Narrow", sans-serif;
    font-weight: 700;
    font-size: 88px;
    line-height: 1;
    color: var(--brand-dark);
    letter-spacing: 0.5px;
    white-space: nowrap;
    transform: translateY(-50%);
  }
  .divider {
    position: absolute;
    left: 0;
    top: 597px;
    width: 1019px;
    height: 3px;
    background: var(--paper-white);
  }
  .card-back {
    position: absolute;
    left: 0;
    top: 601px;
    width: 1019px;
    height: 599px;
    background: var(--ink-black);
  }
  .serif-box {
    position: absolute;
    left: 255px;
    width: 509px;
    background: var(--box-red);
    color: var(--paper-white);
    font-family: "EB Garamond", Garamond, serif;
    text-align: center;
    letter-spacing: 1.5px;
  }
  .name-box {
    top: 36px;
    height: 153px;
  }
  .person-name {
    margin: 4px 0 0;
    font-size: 52px;
    font-weight: 400;
    line-height: 1.1;
  }
  .person-title {
    margin: 10px 0 0;
    font-size: 29px;
    line-height: 1.22;
  }
  .back-wordmark {
    position: absolute;
    left: 0;
    top: 265px;
    width: 1019px;
    margin: 0;
    text-align: center;
    font-family: "Fira Sans Extra Condensed", "Arial Narrow", sans-serif;
    font-weight: 700;
    font-size: 128px;
    line-height: 1;
    color: var(--paper-white);
    letter-spacing: 1px;
    white-space: nowrap;
  }
  .contact-box {
    top: 411px;
    height: 153px;
    padding-top: 4px;
    box-sizing: border-box;
  }
  .contact-list {
    margin: 0;
    font-size: 24.5px;
    line-height: 28px;
    font-style: normal;
  }
  .contact-list span { display: block; }
</style>
</head>
<body>
<main class="canvas">
  <section class="card-front" aria-label="Card front">
    <svg class="front-mark" viewBox="0 0 244 244" aria-hidden="true">
      <circle cx="122" cy="122" r="122" fill="var(--brand-red)"/>
    </svg>
    <h1 class="front-wordmark">BRIGHT LANE TEK</h1>
  </section>

  <div class="divider"></div>

  <section class="card-back" aria-label="Card back">
    <div class="serif-box name-box">
      <p class="person-name">Rafe Tolliverson</p>
      <p class="person-title">Vice-President<br>Bright Lane Tek</p>
    </div>

    <h2 class="back-wordmark">BRIGHT LANE TEK</h2>

    <div class="serif-box contact-box">
      <address class="contact-list">
        <span>3187 Winslow Drive, Suite 412</span>
        <span>Oak Hollow, NJ 07391</span>
        <span>rafe@brightlanetek.example</span>
        <span>Office : 1-855-217-9038 X 414</span>
        <span>Cell number : 908-731-2948</span>
      </address>
    </div>
  </section>
</main>
</body>
</html>
```